Business Card needed for Drainor, a growing Septic Service company

Drainor, a growing local septic service company in Pennsylvania, needs updated business cards. We'd like the business card to feature our logo and communicate that we provide Septic Pumping, Installations/Repairs, Restroom Rentals, and 24/7 Emergency Service. The business card should be eye-catching, bold, and clean/simple. We have been in business almost 10 years and would like to expand and update our business brand and image.

Target Market(s)

Residential and Commercial, New and Current Homeowners

Industry/Entity Type

Service

Contact Information for Business Card

Contact on the business card should be: Dean Harlow Owner & Operator
Phone: 610-555-0187
Email: service@drainor-example.com
Website: www.drainor-example.com
Address: 812 Millbrook Lane Easton PA 18042

Font styles to use
Sans Serif

Colors

Designer to choose colors to be used in the design.

Requirements
Must have
• Feature logo on both side of business card.
Nice to have
• We envision the contact information on one side and our services listed on the other side. Utilize the green from the symbol in our logo as part of the design, overall design color scheme should be white, grey, black.

```html
<!DOCTYPE html>
<html lang="en">
<head>
<meta charset="utf-8">
<title>Drainor – Business Card</title>
<link href="https://fonts.googleapis.com/css2?family=Open+Sans:wght@400;600;800&display=swap" rel="stylesheet">
<style>
  :root {
    --green: #86b130;
    --ink: #222222;
    --grey: #5a5a5a;
    --rule: #8a8a8a;
    --paper: #ffffff;
    --backdrop: #e9e9e9;
  }
  * { box-sizing: border-box; margin: 0; padding: 0; }
  html, body {
    width: 1200px; height: 967px; overflow: hidden;
    background: var(--backdrop);
    font-family: "Open Sans", Arial, sans-serif;
  }
  .sheet {
    width: 1200px; height: 967px;
    display: flex; flex-direction: column; align-items: center; justify-content: center;
    gap: 47px;
  }
  .card {
    position: relative;
    width: 700px; height: 400px;
    box-shadow: 0 6px 18px rgba(0,0,0,.12);
  }
  .card--front { background: var(--paper); }
  .card--back { background: var(--green); }

  .brand {
    position: absolute; display: flex; align-items: center; gap: 18px;
  }
  .brand__mark { width: 58px; height: 58px; }
  .brand__name {
    font-weight: 800; font-size: 76px; letter-spacing: 2px; line-height: 1;
  }
  .card--front .brand { left: 60px; top: 62px; }
  .card--front .brand__mark { background: var(--green); }
  .card--front .brand__name { color: var(--ink); }
  .card--back .brand { left: 120px; top: 110px; }
  .card--back .brand__mark { background: var(--paper); }
  .card--back .brand__name { color: var(--paper); }

  .person { position: absolute; left: 60px; top: 222px; color: var(--grey); font-size: 17px; line-height: 1.45; }
  .person__name { color: var(--green); font-weight: 600; font-size: 25px; line-height: 1.2; margin-bottom: 4px; }

  .divider { position: absolute; left: 345px; top: 222px; width: 1px; height: 120px; background: var(--rule); }

  .contacts { position: absolute; left: 372px; top: 232px; list-style: none; color: var(--grey); font-size: 18px; }
  .contacts li { display: flex; align-items: center; gap: 12px; height: 34px; }
  .contacts svg { width: 18px; height: 18px; fill: var(--green); flex: none; }

  .services {
    position: absolute; left: 120px; top: 226px;
    color: var(--paper); font-size: 19px; line-height: 1.6;
  }
</style>
</head>
<body>
<main class="sheet">
  <section class="card card--front" aria-label="Business card front">
    <div class="brand">
      <span class="brand__mark"></span>
      <span class="brand__name">DRAINOR</span>
    </div>
    <div class="person">
      <p class="person__name">Dean Harlow</p>
      <p>Owner &amp; Operator</p>
      <p>812 Millbrook Lane Easton</p>
      <p>PA 18042</p>
    </div>
    <div class="divider"></div>
    <ul class="contacts">
      <li>
        <svg viewBox="0 0 24 24" aria-hidden="true"><path d="M6.6 10.8a15 15 0 0 0 6.6 6.6l2.2-2.2c.3-.3.7-.4 1-.2 1.1.4 2.3.6 3.6.6.6 0 1 .4 1 1V20c0 .6-.4 1-1 1C10.6 21 3 13.4 3 4c0-.6.4-1 1-1h3.5c.6 0 1 .4 1 1 0 1.3.2 2.5.6 3.6.1.3 0 .7-.2 1z"/></svg>
        (610) 555-0187
      </li>
      <li>
        <svg viewBox="0 0 24 24" aria-hidden="true"><path d="M2 5h20v14H2z M2 5l10 8 10-8" fill="none" stroke="#86b130" stroke-width="2"/></svg>
        service@drainor-example.com
      </li>
      <li>
        <svg viewBox="0 0 24 24" aria-hidden="true"><g fill="none" stroke="#86b130" stroke-width="1.8"><circle cx="12" cy="12" r="9"/><ellipse cx="12" cy="12" rx="4" ry="9"/><path d="M3 12h18M5 7h14M5 17h14"/></g></svg>
        www.drainor-example.com
      </li>
    </ul>
  </section>

  <section class="card card--back" aria-label="Business card back">
    <div class="brand">
      <span class="brand__mark"></span>
      <span class="brand__name">DRAINOR</span>
    </div>
    <div class="services">
      <p>• Septic Pumping • Installations/Repairs</p>
      <p>• Restroom Rentals • 24/7 Emergency Service</p>
    </div>
  </section>
</main>
</body>
</html>
```